Rigboard Media Co Business Card Design

We have a newly created business and logo, but we now need business cards using the new logo.
We are an Australian based business, and we sell advertising space on trucks. The business cards will be seen by media buyers, direct advertisers, fleet owners and business people in general.
Our colours are very simple - black and a strong yellow, with some white. We have chosen the black and yellow for various reasons, but in particular because they are high contrast, and they also have a parallel with the number plates used on our roads, which is relevant to our product offering.
My initial thoughts:
Keep it simple and uncluttered
Use both sides
Our default is Century Gothic
I can provide logo files as required. We do not yet have a website, so I can't direct you there just yet. That may well be another project!
Target Market(s)
The business cards will be seen by media buyers, direct advertisers, fleet owners and business people in general.
Industry/Entity Type
Advertising
Look and feel

```html
<!DOCTYPE html>
<html lang="en">
<head>
<meta charset="utf-8">
<title>Rigboard Media Co – Business Card</title>
<link rel="stylesheet" href="https://fonts.googleapis.com/css2?family=Questrial&display=swap">
<style>
  :root {
    --stage: #e6e3df;
    --card-grey: #a9a9a9;
    --ink: #1e1e1e;
    --band: #262626;
    --yellow: #f5e400;
    --faint: rgba(60, 60, 60, 0.16);
    --font: "Questrial", "Century Gothic", sans-serif;
  }
  html, body {
    margin: 0;
    padding: 0;
    width: 1200px;
    height: 1000px;
    overflow: hidden;
    background: var(--stage);
    font-family: var(--font);
  }
  .canvas {
    position: relative;
    width: 1200px;
    height: 1000px;
  }
  .card {
    position: absolute;
    width: 680px;
    height: 400px;
    background: var(--card-grey);
    box-shadow: 0 6px 18px rgba(0, 0, 0, 0.25);
    overflow: hidden;
  }
  .card--back { left: 50px; top: 60px; }
  .card--front { left: 470px; top: 520px; }

  /* Back side */
  .corner-stripe {
    position: absolute;
    width: 150px;
    height: 120px;
  }
  .corner-stripe--top { right: 0; top: 0; }
  .corner-stripe--bottom { left: 0; bottom: 0; }

  .brand-name {
    position: absolute;
    margin: 0;
    color: var(--ink);
    font-weight: 400;
    letter-spacing: 0.5px;
  }
  .card--back .brand-name {
    left: 58px;
    top: 72px;
    width: 170px;
    font-size: 24px;
    line-height: 1.15;
  }
  .watermark-name {
    position: absolute;
    left: 290px;
    top: 150px;
    margin: 0;
    font-size: 56px;
    line-height: 1.05;
    color: var(--faint);
  }
  .person {
    position: absolute;
    left: 258px;
    top: 44px;
  }
  .person-name {
    margin: 0;
    font-size: 30px;
    color: var(--ink);
    font-weight: 400;
  }
  .person-role {
    margin: 0;
    font-size: 13px;
    color: var(--ink);
  }
  .contact-list {
    position: absolute;
    left: 0;
    top: 0;
    margin: 0;
    padding: 0;
    list-style: none;
  }
  .contact {
    position: absolute;
    display: flex;
    align-items: center;
    gap: 8px;
    font-size: 19px;
    color: var(--ink);
    white-space: nowrap;
  }
  .contact svg { flex: none; }
  .contact--mobile { left: 212px; top: 230px; }
  .contact--email { left: 262px; top: 270px; }
  .contact--landline { left: 330px; top: 318px; }
  .contact--web { left: 398px; top: 356px; }

  /* Front side */
  .card--front .brand-name {
    left: 0;
    right: 0;
    top: 92px;
    text-align: center;
    font-size: 46px;
  }
  .address-band {
    position: absolute;
    left: 0;
    right: 0;
    top: 268px;
    height: 112px;
    background: var(--band);
    display: flex;
    align-items: center;
    justify-content: center;
  }
  .address {
    margin: 0;
    font-style: normal;
    text-align: center;
    color: var(--yellow);
    font-size: 22px;
    line-height: 1.15;
    font-weight: 700;
    letter-spacing: 0.3px;
  }
</style>
</head>
<body>
<main class="canvas">

  <section class="card card--back" aria-label="Business card, contact side">
    <svg class="corner-stripe corner-stripe--top" viewBox="0 0 150 120" aria-hidden="true">
      <path d="M10 0 V70 Q10 100 40 100 H150" fill="none" stroke="var(--ink)" stroke-width="14"/>
      <path d="M10 0 V70 Q10 100 40 100 H150" fill="none" stroke="var(--yellow)" stroke-width="6"/>
    </svg>
    <svg class="corner-stripe corner-stripe--bottom" viewBox="0 0 150 120" aria-hidden="true">
      <path d="M0 20 H110 Q140 20 140 50 V120" fill="none" stroke="var(--ink)" stroke-width="14"/>
      <path d="M0 20 H110 Q140 20 140 50 V120" fill="none" stroke="var(--yellow)" stroke-width="6"/>
    </svg>

    <p class="watermark-name" aria-hidden="true">Rigboard<br>Media Co</p>

    <h2 class="brand-name">Rigboard Media Co</h2>

    <div class="person">
      <h1 class="person-name">Dana Whitlow</h1>
      <p class="person-role">Founder</p>
    </div>

    <ul class="contact-list">
      <li class="contact contact--mobile">
        <svg width="22" height="34" viewBox="0 0 22 34" aria-hidden="true">
          <rect x="1" y="1" width="20" height="32" rx="3" fill="var(--yellow)" stroke="var(--ink)" stroke-width="2"/>
          <rect x="4" y="6" width="14" height="19" fill="var(--ink)"/>
          <circle cx="11" cy="29" r="1.8" fill="var(--ink)"/>
        </svg>
        <span>+61 4 2851 6093</span>
      </li>
      <li class="contact contact--email">
        <svg width="44" height="34" viewBox="0 0 44 34" aria-hidden="true">
          <rect x="1" y="8" width="42" height="25" fill="#f4f4f4" stroke="var(--ink)" stroke-width="1.5"/>
          <path d="M1 8 L22 24 L43 8" fill="none" stroke="var(--ink)" stroke-width="1.5"/>
          <rect x="10" y="1" width="24" height="18" fill="var(--yellow)" stroke="var(--ink)" stroke-width="1.2"/>
          <text x="22" y="15" text-anchor="middle" font-size="13" font-family="sans-serif" fill="var(--ink)">@</text>
        </svg>
        <span>dana@rigboardmedia.com.au</span>
      </li>
      <li class="contact contact--landline">
        <svg width="36" height="36" viewBox="0 0 36 36" aria-hidden="true">
          <circle cx="18" cy="18" r="16" fill="none" stroke="var(--ink)" stroke-width="2"/>
          <path d="M12 10 l4 -1 l2 5 l-3 2 q2 4 5 6 l2 -3 l5 2 l-1 4 q-10 1 -14 -15z" fill="var(--yellow)" stroke="var(--ink)" stroke-width="1"/>
        </svg>
        <span>18000RIGBD</span>
      </li>
      <li class="contact contact--web">
        <svg width="34" height="34" viewBox="0 0 34 34" aria-hidden="true">
          <circle cx="17" cy="17" r="15" fill="var(--ink)"/>
          <ellipse cx="17" cy="17" rx="7" ry="15" fill="none" stroke="#f4f4f4" stroke-width="1.5"/>
          <path d="M2 17 H32 M5 9 H29 M5 25 H29" stroke="#f4f4f4" stroke-width="1.5"/>
        </svg>
        <span>rigboardmedia.com.au</span>
      </li>
    </ul>
  </section>

  <section class="card card--front" aria-label="Business card, brand side">
    <h2 class="brand-name">Rigboard Media Co</h2>
    <div class="address-band">
      <address class="address">
        Rigboard Media Co<br>
        PO Box 2417<br>
        Harbourvale NSW 2096
      </address>
    </div>
  </section>

</main>
</body>
</html>
```